KT Prime Motion personal training needs a new Business Card design for 2016

Business Card design:
Our current business card is very plain
We are bringing on our first team member next year and thought its a perfect time to have a new face lift for our company!

We are a Personal Training business "KT Prime Motion" who specializes in strength and conditioning / weightloss training,
We also run a yearly Bootcamp called "Ferocity Drillcamps", this is our Logo Design which we are looking for

The pink and blue in the logo are our business colours, how ever we don't want those colours to heavily dominate the card.

We are looking for a business card which is eye catching, and creative.

I am open to suggestions and any designs :)

Logo Design:

For our Logo Design we are looking for a bright, energetic logo, preferably a word logo which portrays strength and high intensity
If it has icon's etc in it thats fine again im open for suggestions :)
The Logo Design is for our Bootcamp which runs yearly
The bootcamp is called "Ferocity Drillcamp"

Target Market(s)

Age 20-40
Individuals who want to look great and have more energy

Industry/Entity Type

Business

Contact Information for Business Card

On the front
KT Prime Motion Doriel Maxton Personal Training / Bootcamps / Pilates / Nutrition Healthy mind, Healthy body, Ultimate lifestyle < our slogan
Icons for the following
Email:
Mobile:
Facebook:
Instagram:

On the back we would like to include somewhere
"Show this card to receive 50% off your first 30min pt session"
"Valid to one user only"

Logo Text

Ferocity Drillcamp

Font styles to use
Serif

Colors
e34197
0255a3
000000
ffffff

Requirements
Must have
• - Icons for instagram, facebook, email and mobile phone
• - Slogan: Healthy mind, Healthy body, Ultimate lifestyle
• - What we offer: Personal Training , Bootcamps, Pilates, Nutrition
• - Logo
• -
Nice to have
• - Our 50% offer on the back
• - a place for a photo
Should not have
• - Pink and Blue everywhere

```html
<!DOCTYPE html>
<html lang="en">
<head>
<meta charset="UTF-8">
<title>KT Prime Motion – Business Card</title>
<link href="https://fonts.googleapis.com/css2?family=Saira:wght@400;500;700;800&display=swap" rel="stylesheet">
<style>
  :root {
    --stage: #d9d6d2;
    --card: #1c1c1d;
    --card-back: #141415;
    --gloss: #3a3a3c;
    --pink: #e34197;
    --blue: #2f6bc0;
    --white: #ffffff;
    --grey: #9a9a9c;
    --rule: #4a4a4c;
  }
  * { box-sizing: border-box; margin: 0; padding: 0; }
  html, body { width: 1200px; height: 814px; overflow: hidden; }
  body {
    background: var(--stage);
    font-family: "Saira", Arial, sans-serif;
    position: relative;
  }
  .card {
    position: absolute;
    top: 258px;
    width: 520px;
    height: 298px;
    border-radius: 4px;
    box-shadow: 0 6px 18px rgba(0,0,0,.25);
  }

  /* Back */
  .card--back { left: 60px; background: var(--card-back); }
  .back-brand {
    position: absolute; left: 0; right: 0; top: 52px;
    display: flex; align-items: center; justify-content: center; gap: 12px;
  }
  .back-brand__mark {
    width: 46px; height: 46px; border-radius: 50%; background: var(--gloss);
  }
  .back-brand__name {
    font-weight: 800; font-size: 30px; letter-spacing: .5px;
    color: var(--gloss); text-transform: uppercase;
  }
  .slogan {
    position: absolute; left: 36px; right: 36px; top: 138px;
    font-size: 13.5px; font-weight: 500; color: #d8d8d8;
    letter-spacing: .3px; text-transform: uppercase;
    padding-bottom: 8px; border-bottom: 1px solid var(--rule);
  }
  .offer {
    position: absolute; left: 36px; right: 36px; top: 172px;
    font-size: 13px; color: #cfcfcf;
  }
  .offer strong { font-size: 16px; font-weight: 700; color: var(--white); }
  .offer-note {
    position: absolute; left: 36px; right: 36px; top: 198px;
    text-align: center; font-size: 12px; color: var(--grey);
  }

  /* Front */
  .card--front { left: 620px; background: var(--card); }
  .front-brand {
    position: absolute; left: 30px; top: 96px; width: 240px;
    display: flex; align-items: center; gap: 10px;
  }
  .front-brand__mark {
    width: 44px; height: 44px; border-radius: 50%; background: var(--blue); flex: none;
  }
  .front-brand__name {
    font-weight: 800; font-size: 25px; line-height: 1; color: var(--blue);
    text-transform: uppercase;
  }
  .divider {
    position: absolute; left: 290px; top: 44px; width: 1px; height: 150px;
    background: var(--rule);
  }
  .person { position: absolute; left: 312px; top: 52px; }
  .person__name {
    font-size: 17px; font-weight: 500; color: var(--blue);
    text-transform: uppercase; letter-spacing: .5px; line-height: 1.1;
  }
  .person__role {
    font-size: 13px; color: var(--pink); text-transform: uppercase; line-height: 1.3;
  }
  .contacts { list-style: none; margin-top: 8px; }
  .contacts li {
    display: flex; align-items: center; gap: 8px;
    font-size: 13.5px; color: #e8e8e8; line-height: 21px;
  }
  .contacts svg { width: 12px; height: 12px; flex: none; }
  .icon-box { width: 11px; height: 11px; background: #e8e8e8; border-radius: 2px; flex: none; }
  .services {
    position: absolute; left: 30px; bottom: 40px;
    font-size: 14px; font-weight: 700; color: var(--white);
    text-transform: uppercase; letter-spacing: .3px;
  }
</style>
</head>
<body>

  <section class="card card--back" aria-label="Card back">
    <div class="back-brand">
      <span class="back-brand__mark"></span>
      <span class="back-brand__name">KT Prime Motion</span>
    </div>
    <p class="slogan">Healthy Mind | Healthy Body | Ultimate Lifestyle</p>
    <p class="offer">Show this card to receive <strong>50% off</strong> your first 30min pt session</p>
    <p class="offer-note">Valid to one user only</p>
  </section>

  <section class="card card--front" aria-label="Card front">
    <div class="front-brand">
      <span class="front-brand__mark"></span>
      <span class="front-brand__name">KT Prime Motion</span>
    </div>
    <div class="divider"></div>
    <div class="person">
      <p class="person__name">Doriel Maxton</p>
      <p class="person__role">CEO/Founder</p>
      <ul class="contacts">
        <li>
          <svg viewBox="0 0 12 12"><rect x="3" y="0.5" width="6" height="11" rx="1" fill="none" stroke="#e8e8e8" stroke-width="1.2"/><circle cx="6" cy="9.6" r=".7" fill="#e8e8e8"/></svg>
          555 014 2290
        </li>
        <li><span class="icon-box"></span>ktprimemotion</li>
        <li><span class="icon-box"></span>ktprimemotion</li>
        <li>
          <svg viewBox="0 0 12 12"><rect x=".5" y="2" width="11" height="8" rx="1" fill="#e8e8e8"/><path d="M1 2.5 6 6.5 11 2.5" fill="none" stroke="#1c1c1d" stroke-width="1"/></svg>
          hello@ktprime.example
        </li>
        <li>
          <svg viewBox="0 0 12 12"><circle cx="6" cy="6" r="5.4" fill="none" stroke="#e8e8e8" stroke-width="1.1"/><ellipse cx="6" cy="6" rx="2.3" ry="5.4" fill="none" stroke="#e8e8e8" stroke-width="1"/><path d="M.6 6h10.8" stroke="#e8e8e8" stroke-width="1"/></svg>
          www.ktprime.example
        </li>
      </ul>
    </div>
    <p class="services">Personal Training | Bootcamps | Pilates | Nutrition</p>
  </section>

</body>
</html>
```